KORBALT

The business want a professional looking business card. We have a scetch we will add but want the extra upgrade, and would like more suggestions for variations of our business cards.

```html
<!DOCTYPE html>
<html lang="en">
<head>
<meta charset="utf-8">
<title>KORBALT – Business Card</title>
<link href="https://fonts.googleapis.com/css2?family=Poppins:wght@300;400;500&display=swap" rel="stylesheet">
<style>
  :root {
    --backdrop: #e6dcc0;
    --card-light: #8f6a2c;
    --card-dark: #5c3f17;
    --foil: #e9c462;
    --foil-soft: #d9b255;
    --pattern-light: #c9a24a;
    --pattern-dark: #7a5620;
    --shadow: rgba(70, 50, 20, 0.28);
  }
  * { box-sizing: border-box; margin: 0; padding: 0; }
  html, body {
    width: 1200px;
    height: 900px;
    overflow: hidden;
    background: var(--backdrop);
    font-family: "Poppins", sans-serif;
  }
  .stage {
    position: relative;
    width: 1200px;
    height: 900px;
    display: flex;
    align-items: center;
    justify-content: center;
    gap: 70px;
  }
  .card {
    position: relative;
    background: linear-gradient(135deg, var(--card-light), var(--card-dark));
    box-shadow: 0 18px 40px var(--shadow);
    overflow: hidden;
  }
  /* Front side */
  .card-front {
    width: 320px;
    height: 560px;
  }
  .card-front .pattern-field {
    position: absolute;
    inset: 0;
    background: radial-gradient(circle at 50% 45%, var(--pattern-light), var(--pattern-dark) 85%);
  }
  .card-front .brand-tile {
    position: absolute;
    left: 50%;
    top: 50%;
    width: 190px;
    height: 190px;
    transform: translate(-50%, -50%);
    background: linear-gradient(135deg, var(--card-light), var(--card-dark));
    display: flex;
    align-items: center;
    justify-content: center;
  }
  .brand-tile .brand-name {
    color: var(--foil);
    font-weight: 400;
    font-size: 24px;
    letter-spacing: 4px;
  }
  /* Back side */
  .card-back {
    width: 560px;
    height: 320px;
    padding: 38px 44px;
    color: var(--foil);
  }
  .holder {
    margin-bottom: 22px;
  }
  .holder .role {
    font-size: 12px;
    font-weight: 300;
    letter-spacing: 0.5px;
    color: #f2e3b8;
  }
  .holder .name {
    font-size: 19px;
    font-weight: 400;
    color: #f2e3b8;
  }
  .wordmark {
    font-size: 62px;
    font-weight: 400;
    letter-spacing: 18px;
    line-height: 1;
    color: var(--foil);
  }
  .contact {
    position: absolute;
    right: 60px;
    bottom: 34px;
    list-style: none;
    text-align: center;
    font-size: 13px;
    font-weight: 300;
    line-height: 1.55;
    color: #f2e3b8;
  }
</style>
</head>
<body>
  <main class="stage">
    <section class="card card-front" aria-label="Card front">
      <div class="pattern-field" role="img" aria-label="Gold foil repeating leaf-and-dot ornamental pattern"></div>
      <div class="brand-tile">
        <span class="brand-name">KORBALT</span>
      </div>
    </section>

    <section class="card card-back" aria-label="Card back">
      <div class="holder">
        <p class="role">CEO &amp; Founder</p>
        <p class="name">Aksel Torvik Brennhaug</p>
      </div>
      <h1 class="wordmark">KORBALT</h1>
      <ul class="contact">
        <li>00 47 90 12 34 56</li>
        <li>korbalt.llc@postmail.com</li>
        <li>www.korbalt.llc</li>
      </ul>
    </section>
  </main>
</body>
</html>
```